Marlow Yardcraft need a flyer - A6 - Double sided

We need a flyer that will engage potential customer in need for gardening services. We offer high quality gardening services spanning from lawn mowing and weeding to soil improvement to tree pruning and so on.
I would like a double sided flyer A6 size. I trust your expert touch in terms of lay out but the general idea I had was to have one side with the logo, a catchy picture (or more), the website/phone number/address and on the flip side a little more text focusing on the client perspective with statement such as 'Let us do the hard work so that you can enjoy your garden' (obviously the wording isn't my strongest skill) but the idea is to get into the customer perspective;
I would also like to list all the service we can offer such as but not limited to weeding, pruning, lawn care, green waste disposal, soil improvement, hedging, edging, lawn mowing,...
Happy for you to use any picture free of right from the internet if necessary

Target Market(s)

Home owner & Businesses

Industry/Entity Type

Landscape Gardening

Requirements
Must have
• website - http://yardcraft-marlow.com.au (feel free to browse the website to get ideas on color theme and overall look)
• phone number - (08) 6341 2705
Nice to have
• a list of services on offer
• phone number and website
• being customer perspective focused (the benefits for the customer) - perhaps on the flip side some text like 'highly trained and experienced landscape gardeners so that the job is done perfectly every time', 'always carrying all range of commercial grade tools so that we can tackle any job', 'Experienced gardeners so that the job is achieve faster' (it doesn't have to be in those exact words as I trust that you may be expert in wording as well as designers?)

```html
<!DOCTYPE html>
<html lang="en">
<head>
<meta charset="utf-8">
<title>Marlow Yardcraft – A6 Flyer</title>
<link href="https://fonts.googleapis.com/css2?family=Rubik:wght@400;500;700;900&family=Courgette&display=swap" rel="stylesheet">
<style>
  :root{
    --canvas:#f2f2f2;
    --forest:#425d3b;
    --lime:#9bc34a;
    --charcoal:#282d29;
    --charcoal-soft:#313731;
    --sand:#b99a6c;
    --sand-deep:#a6875a;
    --white:#ffffff;
    --ink:#2a2f2a;
  }
  *{box-sizing:border-box;margin:0;padding:0}
  html,body{width:1200px;height:1000px;overflow:hidden}
  body{background:var(--canvas);position:relative;font-family:"Rubik",Arial,sans-serif;color:var(--ink)}

  .flyer{position:absolute;top:117px;width:548px;height:772px;background:var(--white);overflow:hidden}
  .flyer--front{left:25px}
  .flyer--back{left:627px}

  /* front */
  .front-header{position:absolute;left:0;top:0;width:548px;height:195px;background:var(--forest);display:flex;flex-direction:column;align-items:center;justify-content:center;padding-top:4px}
  .brand-name{color:var(--white);font-weight:900;text-transform:uppercase;text-align:center;line-height:.9;letter-spacing:1px}
  .brand-name__top{display:block;font-size:94px}
  .brand-name__bottom{display:block;font-size:62px}
  .tagline-band{position:absolute;left:0;top:195px;width:548px;height:43px;background:var(--lime);color:var(--white);font-weight:700;font-size:18.5px;letter-spacing:.2px;display:flex;align-items:center;justify-content:center;text-transform:uppercase}
  .photo{position:absolute}
  .photo--gardener{left:0;top:245px;width:352px;height:250px;background:radial-gradient(circle at 62% 38%,#6f6a58 0,#3c4a3a 30%,transparent 55%),linear-gradient(135deg,#4a6a2e,#2f4a24 50%,#1f2a2a)}
  .photo--planting{left:360px;top:245px;width:188px;height:250px;background:radial-gradient(ellipse at 55% 70%,#4a3a2c 0,transparent 45%),linear-gradient(170deg,#7a9a52,#4f7a2e 55%,#5f8f3a)}
  .photo--hose{left:0;top:506px;width:173px;height:125px;background:linear-gradient(180deg,#8fb066 0,#6d9640 45%,#c9a33a 52%,#6d9640 60%,#55802e)}
  .photo--trimmer{left:184px;top:506px;width:165px;height:125px;background:radial-gradient(circle at 70% 60%,#8a8a86 0,transparent 35%),linear-gradient(150deg,#8fb05a,#4e7a2c 60%,#2f3a2a)}
  .photo--mower{left:360px;top:506px;width:188px;height:125px;background:linear-gradient(180deg,#9aa394 0,#7b8a6a 30%,#c9a53a 45%,#b6952f 58%,#5c8f35 70%,#4f8a2e)}

  .contact-bar{position:absolute;left:0;top:641px;width:548px;height:131px;background:var(--charcoal);padding:8px 0 0 26px}
  .contact-bar__heading{font-family:"Courgette",cursive;color:var(--sand);font-size:29px;line-height:40px}
  .contact-line{display:flex;align-items:center;gap:8px;color:var(--white);font-weight:700;font-size:25px;line-height:34px}
  .contact-line svg{width:24px;height:24px;flex:none}
  .social-square{position:absolute;left:483px;width:38px;height:37px;background:var(--sand)}
  .social-square--one{top:20px}
  .social-square--two{top:68px}

  /* back */
  .back-header{position:absolute;left:0;top:0;width:548px;height:199px;background:var(--forest);padding:22px 26px 0;color:var(--white)}
  .back-header__lead{font-weight:700;font-size:24px;line-height:31px;max-width:480px}
  .back-header__cta{font-weight:700;font-size:24px;line-height:31px;margin-top:14px}
  .brand-name--small{margin-top:8px;text-align:left;line-height:.88}
  .brand-name--small .brand-name__top{font-size:35px}
  .brand-name--small .brand-name__bottom{font-size:23px}
  .back-rule{position:absolute;left:0;top:205px;width:548px;height:8px;background:var(--lime)}
  .services{position:absolute;left:0;top:213px;width:548px;height:559px;background:var(--charcoal)}
  .services__texture{position:absolute;inset:0;background:radial-gradient(circle at 20% 30%,var(--charcoal-soft) 0,transparent 30%),radial-gradient(circle at 80% 70%,var(--charcoal-soft) 0,transparent 30%),var(--charcoal)}
  .service-tile{position:absolute;background:var(--sand);display:flex;flex-direction:column;align-items:center;justify-content:flex-end;text-align:center;font-size:18.5px;line-height:19px;color:var(--ink);padding-bottom:20px}
  .service-icon{width:82px;height:58px;background:radial-gradient(ellipse at center,rgba(42,47,42,.55) 0,rgba(42,47,42,.15) 60%,transparent 72%);margin-bottom:12px}
  .tile-1{left:14px;top:28px;width:170px;height:148px;border-radius:40px 26px 46px 30px/30px 44px 28px 40px}
  .tile-2{left:206px;top:26px;width:134px;height:152px;border-radius:30px 42px 28px 38px/40px 26px 44px 30px}
  .tile-3{left:348px;top:24px;width:186px;height:150px;border-radius:44px 30px 40px 28px/28px 40px 30px 46px}
  .tile-4{left:10px;top:192px;width:162px;height:170px;border-radius:30px 46px 34px 40px/44px 30px 40px 28px}
  .tile-5{left:180px;top:196px;width:170px;height:166px;border-radius:46px 30px 42px 34px/32px 44px 30px 40px}
  .tile-6{left:356px;top:204px;width:170px;height:172px;border-radius:34px 40px 30px 46px/40px 30px 46px 32px}
  .tile-7{left:10px;top:370px;width:164px;height:170px;border-radius:40px 30px 46px 34px/30px 42px 32px 44px}
  .tile-8{left:184px;top:372px;width:174px;height:164px;border-radius:30px 44px 34px 40px/42px 30px 44px 30px}
  .tile-2,.tile-8{font-size:17.5px}
  .tile-call{left:372px;top:394px;width:164px;height:150px;border-radius:44px 34px 40px 30px/30px 44px 34px 40px;justify-content:flex-start;padding:18px 0 0}
  .call-heading{font-weight:700;font-size:16px}
  .call-icon{width:58px;height:46px;margin:10px 0 4px}
  .call-number{font-weight:700;font-size:26px;line-height:30px}
</style>
</head>
<body>

<section class="flyer flyer--front">
  <header class="front-header">
    <h1 class="brand-name"><span class="brand-name__top">Marlow</span><span class="brand-name__bottom">Yardcraft</span></h1>
  </header>
  <div class="tagline-band">Affordable and reliable gardening service</div>

  <div class="photo photo--gardener" role="img" aria-label="Photo of a smiling gardener pruning shrubs with secateurs"></div>
  <div class="photo photo--planting" role="img" aria-label="Photo of gloved hands planting into a garden bed"></div>
  <div class="photo photo--hose" role="img" aria-label="Photo of a garden hose nozzle on the lawn"></div>
  <div class="photo photo--trimmer" role="img" aria-label="Photo of hedge trimmers cutting foliage"></div>
  <div class="photo photo--mower" role="img" aria-label="Photo of a ride-on mower cutting a lawn"></div>

  <footer class="contact-bar">
    <p class="contact-bar__heading">Get in touch today!</p>
    <p class="contact-line">
      <svg viewBox="0 0 24 24" aria-hidden="true"><path fill="#b99a6c" d="M3 9c0-3 4-4 9-4s9 1 9 4v2h-5V9.5c-1-.6-2.4-.9-4-.9s-3 .3-4 .9V11H3z"/><path fill="#b99a6c" d="M7 12h10l3 7H4z"/><circle cx="12" cy="15.5" r="2" fill="#282d29"/></svg>
      (08) 6341 2705
    </p>
    <p class="contact-line">
      <svg viewBox="0 0 24 24" aria-hidden="true"><g fill="none" stroke="#b99a6c" stroke-width="2"><circle cx="12" cy="12" r="9"/><ellipse cx="12" cy="12" rx="4" ry="9"/><path d="M3 12h18M5 7h14M5 17h14"/></g></svg>
      www.yardcraft-marlow.com.au
    </p>
    <div class="social-square social-square--one" role="img" aria-label="Social profile"></div>
    <div class="social-square social-square--two" role="img" aria-label="Social profile"></div>
  </footer>
</section>

<section class="flyer flyer--back">
  <header class="back-header">
    <p class="back-header__lead">Don’t let your brown thumb get in the way of having a beautiful garden.</p>
    <p class="back-header__cta">Call in the professionals.</p>
    <p class="brand-name brand-name--small"><span class="brand-name__top">Marlow</span><span class="brand-name__bottom">Yardcraft</span></p>
  </header>
  <div class="back-rule"></div>

  <div class="services">
    <div class="services__texture" role="img" aria-label="Decorative pebble pattern background"></div>
    <div class="service-tile tile-1"><div class="service-icon" role="img" aria-label="Lawn mower icon"></div>Lawn Care</div>
    <div class="service-tile tile-2"><div class="service-icon" role="img" aria-label="Watering can and sprout icon"></div>Tree Pruning<br>and Plant Care</div>
    <div class="service-tile tile-3"><div class="service-icon" role="img" aria-label="Hedge trimmer icon"></div>Hedge Trimming</div>
    <div class="service-tile tile-4"><div class="service-icon" role="img" aria-label="Seedling in hand icon"></div>Organic<br>Gardening</div>
    <div class="service-tile tile-5"><div class="service-icon" role="img" aria-label="Wood chipper icon"></div>Mulching</div>
    <div class="service-tile tile-6"><div class="service-icon" role="img" aria-label="Weeds and grass icon"></div>Weed Control</div>
    <div class="service-tile tile-7"><div class="service-icon" role="img" aria-label="Wheelie bin icon"></div>Green Waste<br>Removal</div>
    <div class="service-tile tile-8"><div class="service-icon" role="img" aria-label="Shovel in soil icon"></div>Fertilising and<br>Soil Improvement</div>
    <div class="service-tile tile-call">
      <p class="call-heading">Call us today!</p>
      <svg class="call-icon" viewBox="0 0 58 46" aria-hidden="true">
        <path fill="#2a2f2a" d="M4 14C4 6 16 3 29 3s25 3 25 11v5H42v-5c-3-2-8-3-13-3s-10 1-13 3v5H4z"/>
        <path fill="#2a2f2a" d="M17 20h24l9 22H8z"/>
        <circle cx="29" cy="31" r="6" fill="#b99a6c"/>
      </svg>
      <p class="call-number">6341 2705</p>
    </div>
  </div>
</section>

</body>
</html>
```